Personal Website for DBA of my main company

I need a website created for my personal brand for one of my DBA's of my main company. This website will be about my personal passion of wine. I am a certified sommelier and want a page that shows my passions for the wine industry. It will consist of pages that have video, pictures and possibly links to my cellar. (I have uploaded a screen shot of the only page I could find from a sommelier, I do not want to copy or look anything like this page....its just an idea of what one would look like)

Target Market(s)

Small, mostly word of mouth customers

Industry/Entity Type

Wine and Service Industry

Coding

Coded - Design and coding required

Number of Pages Required

4 page

Font styles to use
Other font styles liked:
• Font that is current but will be relevant in the future as well

Colors
0054AA
0677BA
7BADD7
CADEEF
E8F1F8
0094D4
00A9DD
6FCCEA
C7EBF8
E9F6FB
00AB8E
00BBA5
67D7C9
C6EFE9
E9F9F6
EB3D1F
EC4F4E
F09395
F8D3D4
FCEDEE

Requirements
Must have
• Landing page, video page and images page.

```html
<!DOCTYPE html>
<html lang="en">
<head>
<meta charset="utf-8">
<title>Veras Wine — Personal Passion of Wine</title>
<link rel="stylesheet" href="https://fonts.googleapis.com/css2?family=Saira:ital,wght@0,600;0,800;1,700;1,800&family=Mulish:wght@400;600;700&display=swap">
<style>
:root{
  --red:#e5473c;
  --red-soft:#f09395;
  --green:#01735a;
  --green-dark:#015a47;
  --ink:#111111;
  --text:#333333;
  --muted:#555555;
  --pale:#eef4f7;
  --white:#ffffff;
  --black:#0c0c0c;
}
*{box-sizing:border-box;margin:0;padding:0}
html,body{width:1200px;height:4549px;overflow:hidden}
body{position:relative;background:var(--white);font-family:"Mulish",sans-serif;color:var(--text)}
.display{font-family:"Saira",sans-serif;font-style:italic;font-weight:800;color:var(--ink)}
.btn{position:absolute;display:flex;align-items:center;justify-content:center;background:var(--red);color:var(--white);
  font-family:"Saira",sans-serif;font-style:italic;font-weight:700;font-size:14px;border-radius:22px;letter-spacing:.3px}
.photo{position:absolute}

/* header */
.brand{position:absolute;left:0;width:1200px;top:20px;text-align:center;font-family:"Saira",sans-serif;font-weight:800;font-size:38px;letter-spacing:1px;color:var(--ink)}
.nav{position:absolute;top:88px;left:326px;display:flex;font-size:13px;font-weight:600;color:var(--ink)}
.nav span{padding:0 22px;border-left:1px solid #999;line-height:20px}
.nav span:first-child{border-left:none;padding-left:4px}
.call{position:absolute;top:84px;left:983px;display:flex;align-items:center;gap:8px;font-size:13px;color:var(--ink)}
.call i{width:30px;height:30px;border-radius:50%;background:var(--red);display:flex;align-items:center;justify-content:center}
.corner-top{position:absolute;left:995px;top:0;width:205px;height:10px;background:var(--red)}
.corner-right{position:absolute;left:1186px;top:0;width:14px;height:459px;background:var(--red)}
.social-rail{position:absolute;left:18px;top:232px;width:300px;transform-origin:0 0;transform:rotate(-90deg) translateX(-290px);
  display:flex;gap:28px;font-size:13px;letter-spacing:2px;color:var(--ink)}

/* hero */
.hero-frame{position:absolute;left:56px;top:526px;width:542px;height:124px;background:var(--red)}
.hero-photo{left:71px;top:122px;width:1058px;height:515px;background:linear-gradient(110deg,#6a4a36 0%,#9b7a5c 30%,#3f5d8c 48%,#7e7a72 70%,#4c4a48 100%)}
.hero-title{position:absolute;left:789px;top:255px;font-size:58px;line-height:62px;color:var(--white)}
.hero-title .sm{font-size:44px}
.dots{position:absolute;left:1033px;top:613px;display:flex;gap:6px}
.dots b{width:6px;height:6px;border-radius:50%;background:var(--white)}
.dots b:first-child{background:var(--red)}

/* about */
.eyebrow{position:absolute;font-size:16px;color:var(--ink);text-transform:uppercase}
.h2{position:absolute;font-size:40px;line-height:44px}
.para{position:absolute;font-size:14px;line-height:21px;color:var(--text)}
.arch{left:700px;top:702px;width:429px;height:509px;border-radius:214px 214px 0 0;background:linear-gradient(160deg,#8a4b3a 0%,#3c5a86 45%,#4e6f7a 70%,#a7552f 100%)}
.dotgrid{position:absolute;background-image:radial-gradient(#222 1.4px,transparent 1.6px);background-size:7px 7px}

/* making */
.making{position:absolute;left:0;top:1287px;width:1200px;height:762px;background:radial-gradient(ellipse at 50% 40%,#0b8a6c 0%,var(--green) 55%,var(--green-dark) 100%)}
.making .title{position:absolute;left:0;width:1200px;top:28px;text-align:center;font-size:42px;color:var(--white)}
.making .sub{position:absolute;left:0;width:1200px;top:97px;text-align:center;font-size:14px;color:var(--white)}
.vineyard{left:160px;top:141px;width:880px;height:436px;background:linear-gradient(100deg,#8fa38a 0%,#5a6f8e 28%,#3b4f38 50%,#3c3b66 70%,#6f8a3e 100%)}
.stat{position:absolute;top:612px;width:200px;text-align:center;color:var(--white)}
.stat svg{display:block;margin:0 auto 4px}
.stat strong{display:block;font-size:22px;font-weight:600}
.stat span{font-size:12px}

/* quality */
.feature{position:absolute;width:230px;text-align:center}
.feature svg{display:block;margin:0 auto 6px}
.feature h3{font-family:"Saira",sans-serif;font-style:italic;font-weight:800;font-size:21px;color:var(--ink);margin-bottom:6px}
.feature p{font-size:12.5px;line-height:19px;color:var(--text)}

/* collection */
.collection{position:absolute;left:0;top:2559px;width:1200px;height:530px;background:var(--pale)}
.section-title{position:absolute;left:0;width:1200px;text-align:center;font-size:42px}
.card{position:absolute;top:106px;width:247px}
.card .art{height:286px;border-radius:124px 124px 0 0;background:var(--red);position:relative;overflow:hidden}
.card .art::before{content:"";position:absolute;left:14px;right:14px;top:18px;bottom:18px;border:1.5px solid rgba(255,255,255,.75);border-radius:110px 110px 0 0}
.card .bottle{position:absolute;left:104px;top:36px;width:40px;height:274px;border-radius:12px 12px 8px 8px}
.card h4{margin-top:38px;text-align:center;font-family:"Saira",sans-serif;font-style:italic;font-weight:800;font-size:21px;color:var(--ink)}
.card p{text-align:center;font-size:12px;color:var(--muted);margin-top:2px}

/* blog */
.post{position:absolute;width:518px;height:155px}
.post .thumb{position:absolute;left:0;top:0;width:247px;height:155px}
.post .meta{position:absolute;left:270px;top:0;font-size:10.5px;color:var(--ink)}
.post .meta em{font-style:normal;color:var(--red)}
.post h5{position:absolute;left:270px;top:20px;width:250px;font-family:"Saira",sans-serif;font-style:italic;font-weight:800;font-size:20px;line-height:26px;color:var(--ink)}
.post p{position:absolute;left:270px;top:88px;width:230px;font-size:12px;line-height:17px}
.post .more{position:absolute;left:270px;top:130px;font-family:"Saira",sans-serif;font-style:italic;font-weight:700;font-size:11px;color:var(--red)}
.rule{position:absolute;height:1px;background:#ddd}

/* contact */
.contact{position:absolute;left:0;top:3685px;width:1200px;height:445px;background:linear-gradient(180deg,#02735a 0%,#046650 100%)}
.contact .title{position:absolute;left:0;width:1200px;top:90px;text-align:center;font-size:42px;color:var(--white)}
.contact .sub{position:absolute;left:0;width:1200px;top:148px;text-align:center;font-size:14px;color:var(--white)}
.field{position:absolute;border:1.5px solid var(--white);color:var(--white);font-size:11px;padding:10px 12px}
.submit{position:absolute;background:var(--white);color:var(--ink);font-size:13px;display:flex;align-items:center;justify-content:center}

/* footer */
.footer{position:absolute;left:0;top:4130px;width:1200px;height:419px;background:var(--black);color:var(--white)}
.footer .logo{position:absolute;left:71px;top:58px;font-family:"Saira",sans-serif;font-weight:800;font-size:38px}
.footer .blurb{position:absolute;left:71px;top:116px;width:250px;font-size:12px;line-height:19px}
.footer .circles{position:absolute;left:71px;top:190px;display:flex;gap:10px}
.footer .circles i{width:36px;height:36px;border-radius:50%;border:1.5px solid #1fb59a}
.footer h6{position:absolute;top:58px;font-family:"Saira",sans-serif;font-style:italic;font-weight:700;font-size:19px;color:var(--red)}
.links{position:absolute;left:409px;top:106px;font-size:12px;line-height:27px;list-style:none}
.info{position:absolute;left:590px;display:flex;gap:10px;font-size:12px;line-height:17px;align-items:center}
.info i{width:30px;height:30px;border-radius:50%;background:#1fb59a;display:flex;align-items:center;justify-content:center;flex:none}
.news-input{position:absolute;left:882px;top:106px;width:247px;height:36px;background:var(--white);color:#555;font-size:11px;padding:11px 10px}
.news-btn{position:absolute;left:882px;top:150px;width:247px;height:36px;background:var(--red);font-size:12px;display:flex;align-items:center;justify-content:center}
.footer .divider{position:absolute;left:71px;top:312px;width:1058px;height:1px;background:#333}
.footer .copy{position:absolute;left:0;width:1200px;top:346px;text-align:center;font-size:12px}
.footer .copy em{font-style:normal;color:var(--red)}
</style>
</head>
<body>

<!-- header -->
<div class="corner-top"></div>
<div class="corner-right"></div>
<div class="brand">VERAS</div>
<nav class="nav"><span>HOME</span><span>ABOUT ME</span><span>WINE</span><span>SERVICES</span><span>BLOG</span><span>CONTACT US</span></nav>
<div class="call"><i><svg width="14" height="14" viewBox="0 0 24 24"><path fill="#fff" d="M6.6 10.8a15 15 0 0 0 6.6 6.6l2.2-2.2c.3-.3.7-.4 1-.2 1.1.4 2.3.6 3.6.6.6 0 1 .4 1 1V20c0 .6-.4 1-1 1A17 17 0 0 1 3 4c0-.6.4-1 1-1h3.5c.6 0 1 .4 1 1 0 1.3.2 2.5.6 3.6.1.3 0 .7-.2 1z"/></svg></i>+1 (555) 402 7719</div>
<div class="social-rail"><span>JOURNAL</span><span>UPDATES</span><span>GALLERY</span></div>

<!-- hero -->
<div class="hero-frame"></div>
<div class="photo hero-photo" role="img" aria-label="Sommelier in a restaurant tasting wine and holding a bottle of white wine"></div>
<h1 class="display hero-title"><span class="sm">Personal</span><br>Passion of<br>Wine</h1>
<div class="btn" style="left:789px;top:453px;width:132px;height:38px">GET STARTED</div>
<div class="dots"><b></b><b></b><b></b></div>

<!-- about -->
<div class="eyebrow" style="left:71px;top:796px">About me</div>
<h2 class="display h2" style="left:71px;top:820px">Veras Wine</h2>
<p class="para" style="left:71px;top:900px;width:510px">Sed ut perspiciatis unde omnis iste natus error sit voluptatem accusantium doloremque laudantium, totam rem aperiam, eaque ipsa quae ab illo inventore veritatis et quasi architecto beatae vitae dicta sunt explicabo.</p>
<p class="para" style="left:71px;top:994px;width:510px">Nemo enim ipsam voluptatem quia voluptas sit aspernatur aut odit aut fugit, sed quia consequuntur magni dolores eos qui ratione voluptatem sequi nesciunt.</p>
<div class="btn" style="left:71px;top:1095px;width:132px;height:40px">READ MORE</div>
<div class="dotgrid" style="left:665px;top:968px;width:70px;height:58px"></div>
<div class="photo arch" role="img" aria-label="Sommelier holding a wine bottle in front of a patterned tapestry wall"></div>
<div class="dotgrid" style="left:1106px;top:1160px;width:54px;height:60px"></div>

<!-- wine making -->
<section class="making">
  <h2 class="display title">The Wine Making</h2>
  <p class="sub">Sed ut perspiciatis unde omnis iste natus error sit voluptatem accusantium doloremque laudantium</p>
  <div class="photo vineyard" role="img" aria-label="Winemaker inspecting ripe dark grape clusters on the vine"></div>
  <div class="stat" style="left:94px"><svg width="52" height="44" viewBox="0 0 52 44" fill="none" stroke="#fff" stroke-width="2"><circle cx="26" cy="24" r="6"/><path d="M14 42c0-7 5-11 12-11s12 4 12 11"/><path d="M26 3l2 4 4 .5-3 3 .8 4-3.8-2-3.8 2 .8-4-3-3 4-.5z"/><path d="M10 10l1.5 3 3 .4-2.2 2 .6 3-2.9-1.5-2.9 1.5.6-3-2.2-2 3-.4zM42 10l1.5 3 3 .4-2.2 2 .6 3-2.9-1.5-2.9 1.5.6-3-2.2-2 3-.4z"/></svg><strong>10+</strong><span>Years of Experience</span></div>
  <div class="stat" style="left:364px"><svg width="52" height="44" viewBox="0 0 52 44" fill="none" stroke="#fff" stroke-width="2"><circle cx="26" cy="12" r="9"/><circle cx="26" cy="10" r="3"/><path d="M21 17c1-3 9-3 10 0"/><path d="M6 32h10l8 4h10c2 0 2-3 0-3h-7M16 32l8-5h6"/><path d="M6 28v12"/></svg><strong>800 K</strong><span>Regular Customer</span></div>
  <div class="stat" style="left:634px"><svg width="52" height="44" viewBox="0 0 52 44" fill="none" stroke="#fff" stroke-width="2"><path d="M4 18l10-8 8 4 8-4 8 4 10 4M14 10l-8 14 14 12 6-4M48 18l-8 10-12 8"/><path d="M20 20l8 8M24 18l8 8"/></svg><strong>250+</strong><span>Worldwide Partner</span></div>
  <div class="stat" style="left:904px"><svg width="52" height="44" viewBox="0 0 52 44" fill="none" stroke="#fff" stroke-width="2"><path d="M12 42V16a14 14 0 0 1 28 0v26z"/><path d="M26 6v36M19 20v10M33 20v10M26 14h-5M26 14h5"/></svg><strong>5+</strong><span>Wine Store</span></div>
</section>

<!-- quality -->
<div class="feature" style="left:79px;top:2124px">
  <svg width="46" height="60" viewBox="0 0 46 60" fill="none" stroke="#e5473c" stroke-width="2"><circle cx="20" cy="18" r="9"/><path d="M11 14c2-8 16-8 18 0"/><path d="M4 58V44c0-6 6-10 16-10s16 4 16 10v14"/><path d="M36 36h8l-1 8c0 3-6 3-6 0zM40 46v8M36 54h8"/></svg>
  <h3>Best Winemaker</h3><p>But I must explain to you how all this mistaken idea of denouncing pleasure and praising</p></div>
<div class="feature" style="left:349px;top:2124px">
  <svg width="46" height="60" viewBox="0 0 46 60" fill="none" stroke="#e5473c" stroke-width="2"><path d="M12 2h6v12l4 6v38H6V20l4-6V2z"/><path d="M6 30h16v14H6z"/><path d="M28 30h14l-1 10c0 6-12 6-12 0zM35 46v10M30 56h10"/></svg>
  <h3>Full of Taste</h3><p>But I must explain to you how all this mistaken idea of denouncing pleasure and praising</p></div>
<div class="feature" style="left:79px;top:2311px">
  <svg width="56" height="56" viewBox="0 0 56 56" fill="none" stroke="#e5473c" stroke-width="2"><path d="M28 4l6 6 8-1 2 8 7 5-4 7 2 8-8 3-3 7-8-2-6 5-6-5-8 2-3-7-8-3 2-8-4-7 7-5 2-8 8 1z"/><path d="M28 18l3 6 7 1-5 5 1 7-6-3-6 3 1-7-5-5 7-1z"/></svg>
  <h3>Hgh Quality</h3><p>But I must explain to you how all this mistaken idea of denouncing pleasure and praising</p></div>
<div class="feature" style="left:349px;top:2311px">
  <svg width="46" height="56" viewBox="0 0 46 56" fill="none" stroke="#e5473c" stroke-width="2"><path d="M23 2v8M23 6l6-3"/><circle cx="17" cy="15" r="5"/><circle cx="29" cy="15" r="5"/><circle cx="11" cy="25" r="5"/><circle cx="23" cy="25" r="5"/><circle cx="35" cy="25" r="5"/><circle cx="17" cy="35" r="5"/><circle cx="29" cy="35" r="5"/><circle cx="23" cy="45" r="5"/></svg>
  <h3>Fresh Fruit</h3><p>But I must explain to you how all this mistaken idea of denouncing pleasure and praising</p></div>
<div class="eyebrow" style="left:700px;top:2178px">Quality</div>
<h2 class="display h2" style="left:700px;top:2200px">For The Best</h2>
<p class="para" style="left:700px;top:2280px;width:420px">Sed ut perspiciatis unde omnis iste natus error sit voluptatem accusantium doloremque laudantium, totam rem aperiam, eaque ipsa quae ab illo inventore veritatis et quasi architecto beatae vitae dicta sunt explicabo.</p>
<div class="btn" style="left:700px;top:2410px;width:132px;height:40px">READ MORE</div>

<!-- collection -->
<section class="collection">
  <h2 class="display section-title" style="top:30px">Latest Collection</h2>
  <div class="card" style="left:71px"><div class="art"></div><div class="bottle" role="img" aria-label="Bottle of red wine with a cream label" style="background:linear-gradient(90deg,#3a0f14,#7a2430 50%,#3a0f14)"></div><h4>Circumstances</h4><p>Duis aute irure dolor in reprehenderit</p></div>
  <div class="card" style="left:341px"><div class="art"></div><div class="bottle" role="img" aria-label="Bottle of white wine with a white label" style="background:linear-gradient(90deg,#8b8a2a,#d8d46a 50%,#8b8a2a)"></div><h4>Denouncing</h4><p>Duis aute irure dolor in reprehenderit</p></div>
  <div class="card" style="left:611px"><div class="art"></div><div class="bottle" role="img" aria-label="Dark wine bottle with a black label" style="background:linear-gradient(90deg,#0b0b0b,#3a3a3a 50%,#0b0b0b)"></div><h4>Laboriosam</h4><p>Duis aute irure dolor in reprehenderit</p></div>
  <div class="card" style="left:881px"><div class="art"></div><div class="bottle" role="img" aria-label="Dark red wine bottle with a grey label" style="background:linear-gradient(90deg,#120a18,#3c2538 50%,#120a18)"></div><h4>Magnam</h4><p>Duis aute irure dolor in reprehenderit</p></div>
</section>

<!-- blog -->
<h2 class="display section-title" style="top:3150px">Recent Blog</h2>
<article class="post" style="left:71px;top:3248px"><div class="thumb" role="img" aria-label="Wine bottles resting in a dark cellar rack" style="background:linear-gradient(120deg,#2a1c14,#6e4a2c 50%,#1b1410)"></div><div class="meta">14th Aug, <em>2022</em></div><h5>Excepteur sint occaecat cupidatat non</h5><p>Sed ut perspiciatis unde omnis iste natus error sit voluptatem accusantium</p><div class="more">READ MORE</div></article>
<article class="post" style="left:611px;top:3248px"><div class="thumb" role="img" aria-label="Vineyard rows with purple grape clusters" style="background:linear-gradient(120deg,#4a5a3a,#3b3558 45%,#7a8a4a)"></div><div class="meta">14th Aug, <em>2022</em></div><h5>Excepteur sint occaecat cupidatat non</h5><p>Sed ut perspiciatis unde omnis iste natus error sit voluptatem accusantium</p><div class="more">READ MORE</div></article>
<div class="rule" style="left:341px;top:3426px;width:248px"></div>
<div class="rule" style="left:881px;top:3426px;width:248px"></div>
<article class="post" style="left:71px;top:3451px"><div class="thumb" role="img" aria-label="Rows of oak wine barrels in a cellar" style="background:linear-gradient(120deg,#5a3a24,#a8744a 50%,#3a2416)"></div><div class="meta">14th Aug, <em>2022</em></div><h5>Excepteur sint occaecat cupidatat non</h5><p>Sed ut perspiciatis unde omnis iste natus error sit voluptatem accusantium</p><div class="more">READ MORE</div></article>
<article class="post" style="left:611px;top:3451px"><div class="thumb" role="img" aria-label="Glass of white wine on a dimly lit table" style="background:linear-gradient(120deg,#2a1a0c,#9a6a2a 50%,#1a120a)"></div><div class="meta">14th Aug, <em>2022</em></div><h5>Excepteur sint occaecat cupidatat non</h5><p>Sed ut perspiciatis unde omnis iste natus error sit voluptatem accusantium</p><div class="more">READ MORE</div></article>

<!-- contact -->
<section class="contact">
  <h2 class="display title">CONTACT ME</h2>
  <p class="sub">Sed ut perspiciatis unde omnis iste natus error sit voluptatem</p>
  <div class="field" style="left:228px;top:187px;width:367px;height:43px">Name:</div>
  <div class="field" style="left:228px;top:244px;width:367px;height:43px">Email:</div>
  <div class="field" style="left:228px;top:300px;width:367px;height:43px">Phone:</div>
  <div class="field" style="left:605px;top:187px;width:367px;height:100px">Message:</div>
  <div class="submit" style="left:605px;top:300px;width:367px;height:43px">SUBMIT</div>
</section>

<!-- footer -->
<footer class="footer">
  <div class="logo">VERAS</div>
  <p class="blurb">Sed ut perspiciatis unde omnis iste natus error sit voluptatem accusantium doloremque laudantium</p>
  <div class="circles"><i></i><i></i><i></i></div>
  <h6 style="left:409px">Quick Links</h6>
  <ul class="links"><li>Home</li><li>About Me</li><li>Wine</li><li>Service</li><li>Blog</li><li>Contact Us</li></ul>
  <h6 style="left:590px">Contact Us</h6>
  <div class="info" style="top:106px"><i><svg width="12" height="14" viewBox="0 0 24 28"><path fill="#fff" d="M12 0a10 10 0 0 0-10 10c0 8 10 18 10 18s10-10 10-18A10 10 0 0 0 12 0zm0 14a4 4 0 1 1 0-8 4 4 0 0 1 0 8z"/></svg></i><span>48 Harrow Lane Ashcombe,<br>Kestrel 12AB UK</span></div>
  <div class="info" style="top:164px"><i><svg width="12" height="12" viewBox="0 0 24 24"><path fill="#fff" d="M6.6 10.8a15 15 0 0 0 6.6 6.6l2.2-2.2c.3-.3.7-.4 1-.2 1.1.4 2.3.6 3.6.6.6 0 1 .4 1 1V20c0 .6-.4 1-1 1A17 17 0 0 1 3 4c0-.6.4-1 1-1h3.5c.6 0 1 .4 1 1 0 1.3.2 2.5.6 3.6.1.3 0 .7-.2 1z"/></svg></i><span>+1 (555) 402 7719</span></div>
  <div class="info" style="top:214px"><i><svg width="13" height="10" viewBox="0 0 26 20"><path fill="none" stroke="#fff" stroke-width="2.4" d="M2 2h22v16H2zM2 2l11 9 11-9"/></svg></i><span>hello@verascellar.com</span></div>
  <h6 style="left:882px">Newsletter</h6>
  <div class="news-input">Enter Your Email</div>
  <div class="news-btn">SUBSCRIBE</div>
  <div class="divider"></div>
  <p class="copy">Copyright © 2022 <em>VERAS</em>. All Rights Reserved.</p>
</footer>

</body>
</html>
```